Calloway Dental Care

I need a nice business card design that is double sided. This is for a dental surgery. I have already had a logo designed and just need the business card put together.

It needs to be in a format such that I can make new business cards if new dentists begin working for me. Hence I need to be able to change the text in order to have new names written on new cards.

The front will have the following text:

Dr Tariq Mansour
B. Med. Sci. QBTU B.Dent. Brel. Uni

The logo will appear somewhere on the front. This is attached.

In addition will be the following writing that also needs to appear on the front of the card, perhaps at the bottom on the left side will be:

Shop 4, 212-240 Parlow Street, North Sydney, NSW, 2060

and at the bottom on the right side will be:
(02) 5550 1736
e: info@callowaydentalcare.com.au
www.callowaydentalcare.com.au

On the back of the card will be a section for a map to be drawn (I have uploaded a picture) and also a section written as follows:

"Your next appointment is: (a line needs to be here to write date and time)"

Also I need two lines for two appointments to be written.

Thanks for your efforts!

```html
<!DOCTYPE html>
<html lang="en">
<head>
<meta charset="utf-8">
<title>Calloway Dental Care – Business Card</title>
<link rel="stylesheet" href="https://fonts.googleapis.com/css2?family=Arimo&family=Tinos:wght@400;700&display=swap">
<style>
  :root {
    --paper: #ffffff;
    --ink: #222222;
    --gold: #e9a93a;
    --frame: #efe6d6;
    --navy: #2e3540;
    --line-light: #e9ecef;
  }
  * { margin: 0; padding: 0; box-sizing: border-box; }
  html, body { width: 1200px; height: 663px; overflow: hidden; background: var(--paper); }
  .card {
    position: relative;
    width: 1200px;
    height: 663px;
    background: var(--paper);
    overflow: hidden;
    font-family: "Tinos", "Times New Roman", serif;
    color: var(--ink);
  }
  .logo-spot {
    position: absolute;
    left: 40px; top: 11px;
    width: 331px; height: 128px;
    border: 11px solid var(--frame);
    display: flex; align-items: center; justify-content: center;
    font-family: "Arimo", Arial, sans-serif;
    font-size: 62px;
    color: var(--ink);
  }
  .practice-name {
    position: absolute;
    left: 45px; top: 156px;
    font-weight: 700;
    font-size: 27px;
  }
  .address {
    position: absolute;
    left: 56px; top: 248px;
    font-style: normal;
    font-size: 27px;
    line-height: 50px;
  }
  .dentist {
    position: absolute;
    left: 607px; top: 138px;
  }
  .dentist-name {
    font-weight: 400;
    font-size: 40px;
    color: var(--gold);
    line-height: 50px;
  }
  .qualifications {
    list-style: none;
    margin-top: 12px;
    font-size: 44px;
    line-height: 80px;
  }
  .wave {
    position: absolute;
    left: 0; top: 0;
    width: 1200px; height: 663px;
  }
  .contact-strip {
    position: absolute;
    left: 0; right: 0; top: 612px;
    text-align: center;
    font-family: "Arimo", Arial, sans-serif;
    font-size: 21px;
    letter-spacing: 0.4px;
    color: var(--gold);
    white-space: nowrap;
  }
  .contact-strip .label { letter-spacing: 3px; margin-right: 6px; }
</style>
</head>
<body>
  <main class="card">
    <svg class="wave" viewBox="0 0 1200 663" aria-hidden="true">
      <path d="M0 462 C 320 442, 760 462, 1200 520 L1200 663 L0 663 Z" fill="var(--navy)"/>
      <path d="M0 454 C 340 434, 780 456, 1200 508" fill="none" stroke="var(--paper)" stroke-width="6"/>
      <path d="M0 449 C 340 429, 780 451, 1200 500" fill="none" stroke="var(--gold)" stroke-width="3"/>
      <path d="M0 480 C 360 462, 800 482, 1200 536" fill="none" stroke="var(--line-light)" stroke-width="3"/>
      <path d="M0 497 C 380 479, 820 501, 1200 562" fill="none" stroke="var(--line-light)" stroke-width="2"/>
      <path d="M0 509 C 400 491, 840 515, 1200 583" fill="none" stroke="var(--gold)" stroke-width="2"/>
      <path d="M0 523 C 420 507, 860 531, 1200 602" fill="none" stroke="var(--line-light)" stroke-width="1.5"/>
    </svg>

    <div class="logo-spot">logo</div>

    <p class="practice-name">Calloway Dental care</p>

    <address class="address">
      Shop 4,<br>
      212-240 Parlow Street,<br>
      North Sydney, NSW, 2060
    </address>

    <section class="dentist">
      <h1 class="dentist-name">Dr. Tariq Mansour</h1>
      <ul class="qualifications">
        <li>B. Med. Sci.</li>
        <li>QBTU B.Dent.</li>
        <li>Brel. Uni</li>
      </ul>
    </section>

    <p class="contact-strip">
      <span class="label">Consult</span>(02) 5550 1736 e: info@callowaydentalcare.com.au &nbsp;www.callowaydentalcare.com.au
    </p>
  </main>
</body>
</html>
```